www.velmornit.com

Website design for IT outsourcing company (Velmorn IT)
Pages: Home, About Us, Services, Case Studies, Careers, Contact and more (see current website for guidance)
Include client testimonials
Include client logos (e.g., Plumtrex, etc)
List of services (staffing, app dev, integration, cloud)
Modern, clean, professional design
Blue/white/gray color scheme
Mobile and desktop responsive
Include call-to-action buttons
Space for case studies/project highlights

```html
<!DOCTYPE html>
<html lang="en">
<head>
<meta charset="utf-8">
<title>Velmorn IT – Smart, Scalable IT Solutions</title>
<link href="https://fonts.googleapis.com/css2?family=Montserrat:wght@300;400;600;700;800&family=Roboto:wght@400;500;700&display=swap" rel="stylesheet">
<style>
:root{
  --navy:#0f1a45;
  --navy-deep:#0a1236;
  --blue:#7fb2cf;
  --blue-mid:#5d97bb;
  --ink:#1b1f2a;
  --text:#4a4f5c;
  --muted:#8a8f99;
  --gray-bg:#f3f4f6;
  --white:#ffffff;
  --star:#f5a623;
}
*{margin:0;padding:0;box-sizing:border-box}
html,body{width:1200px;height:4677px;overflow:hidden}
body{position:relative;background:var(--white);font-family:'Roboto',sans-serif;color:var(--text)}
.abs{position:absolute}
.heading{font-family:'Montserrat',sans-serif;color:var(--ink)}
.heading b{font-weight:800}
.heading span{font-weight:400}
.underline{position:absolute;height:3px;width:56px;background:var(--blue);left:50%;transform:translateX(-50%)}

/* hero */
.hero-photo{left:0;top:0;width:1200px;height:760px;background:linear-gradient(90deg,#f4f6f8 0%,#eef1f4 38%,#d9dfe5 55%,#b9a68a 70%,#8a8f96 85%,#c9cfd6 100%)}
.brand{font-family:'Montserrat',sans-serif;font-weight:800;color:var(--blue-mid);letter-spacing:1px}
.brand-mark{width:40px;height:40px;background:var(--blue);border-radius:50%}
.nav{top:58px;left:414px;display:flex;gap:30px;font-size:14px;font-weight:500;color:var(--ink)}
.nav .active{color:var(--blue-mid)}
.talk{left:958px;top:49px;width:131px;height:40px;background:var(--blue);color:var(--navy);font-size:14px;font-weight:500;display:flex;align-items:center;justify-content:center}
.hero-title{left:112px;top:202px;font-family:'Montserrat',sans-serif;font-size:41px;line-height:55px;color:var(--ink);font-weight:400}
.hero-title b{font-weight:800}
.hero-quote{left:112px;top:382px;width:440px;font-size:16px;line-height:28px;color:var(--ink)}
.btn-slant{background:var(--blue);color:var(--navy);font-family:'Montserrat',sans-serif;font-weight:700;font-size:14px;display:flex;align-items:center;padding-left:33px;clip-path:polygon(0 0,84% 0,100% 100%,0 100%)}

/* about */
.about-photo{left:112px;top:771px;width:468px;height:463px;background:linear-gradient(180deg,#8db8d2,#4f86aa)}
.about-text{left:657px;top:900px;width:440px;font-size:13.5px;line-height:24px;color:var(--text)}
.about-text p{margin-bottom:14px}

/* services */
.svc{width:250px;text-align:center;color:var(--white)}
.svc-ring{width:156px;height:156px;margin:0 auto;border-radius:50%;border:3px solid var(--blue);display:flex;align-items:center;justify-content:center}
.svc-core{width:132px;height:132px;border-radius:50%;border:2px solid var(--white);background:var(--navy);display:flex;align-items:center;justify-content:center}
.svc-core.on{background:var(--blue)}
.svc h3{font-size:16px;font-weight:700;line-height:24px;margin:24px 0 12px}
.svc p{font-size:13.5px;line-height:22px;color:#dfe4ef;padding:0 6px}
.pill{display:inline-block;margin-top:22px;width:132px;height:38px;line-height:34px;border:2px solid var(--blue);border-radius:20px;color:var(--blue);font-size:13px;font-weight:700;letter-spacing:.5px}
.pill.on{background:var(--blue);color:var(--white)}

/* testimonials */
.t-card{width:408px;height:231px;background:var(--white);border-radius:22px;box-shadow:0 6px 18px rgba(15,26,69,.18)}
.t-avatar{width:117px;height:117px;border-radius:50%;background:linear-gradient(160deg,#c9ced4,#6d7580)}
.t-body{left:100px;top:30px;width:280px}
.t-quote{font-family:'Montserrat',sans-serif;font-size:60px;font-weight:800;color:var(--blue);line-height:40px;height:40px}
.t-body p{font-size:13.5px;line-height:23px;color:var(--text);margin-top:8px}
.t-name{font-size:16px;font-weight:700;color:var(--ink);margin-top:14px}
.stars{color:var(--star);font-size:17px;letter-spacing:2px}
.arrow-big{font-size:40px;color:var(--muted);font-family:'Montserrat',sans-serif;font-weight:300}

/* clients */
.client-band{left:0;top:2686px;width:1200px;height:300px;background:var(--gray-bg)}
.logo-card{top:2838px;width:165px;height:84px;background:var(--white);border-radius:6px;box-shadow:0 4px 10px rgba(0,0,0,.08);display:flex;align-items:center;justify-content:center;gap:8px;font-size:20px;font-weight:500;color:var(--navy)}
.logo-card i{width:14px;height:14px;border-radius:50%;background:var(--blue-mid);display:block}
.circ-arrow{width:34px;height:34px;border-radius:50%;background:var(--white);box-shadow:0 2px 6px rgba(0,0,0,.15);display:flex;align-items:center;justify-content:center}

/* case studies */
.case{top:3155px;width:311px;height:366px}
.case-img{left:0;top:0;width:311px;height:223px}
.case-box{left:0;top:167px;width:292px;height:199px;background:var(--white);box-shadow:0 4px 14px rgba(0,0,0,.1);padding:28px 28px}
.case-meta{font-size:12.5px;color:var(--ink)}
.case-box h4{font-size:17px;line-height:26px;color:var(--ink);font-weight:700;margin:14px 0 12px}
.case-box p{font-size:13px;line-height:22px;color:var(--text)}

/* contact */
.field{background:var(--white);border:1px solid #cfd6dd;font-size:13px;color:var(--muted);padding:0 20px;display:flex;align-items:center}
.submit{left:506px;top:4134px;width:186px;height:52px;background:var(--navy);border-radius:26px;color:var(--white);font-size:14px;font-weight:700;display:flex;align-items:center;justify-content:center;letter-spacing:.5px}

/* footer */
.f-col h5{font-size:15px;font-weight:700;color:var(--ink);margin-bottom:22px}
.f-col li{list-style:none;font-size:13px;color:var(--text);line-height:27.5px}
.f-contact{font-size:12.5px;color:var(--text);line-height:18px}
.f-contact b{display:block;color:var(--ink);font-weight:700;font-size:12px}
.social{width:30px;height:30px;border-radius:50%;border:1px solid #bfc5cc}
</style>
</head>
<body>

<!-- HERO -->
<div class="abs hero-photo" role="img" aria-label="Photo of a team of developers working together at a laptop in a bright office"></div>
<svg class="abs" style="left:0;top:600px" width="1200" height="170" viewBox="0 0 1200 170">
  <polygon points="0,110 230,35 1200,160 1200,170 0,170" fill="#7fb2cf"/>
  <polygon points="0,130 230,50 1200,168 1200,170 0,170" fill="#ffffff"/>
</svg>
<div class="abs" style="left:112px;top:20px;width:110px;text-align:center">
  <div class="brand-mark" style="margin:14px auto 10px"></div>
  <div class="brand" style="font-size:15px">VELMORNIT</div>
</div>
<nav class="abs nav">
  <span class="active">Home</span><span>About Us</span><span>Services</span><span>Case Studies</span><span>Careers</span><span>Contact</span>
</nav>
<div class="abs talk">Let's Talk</div>
<h1 class="abs hero-title"><b>SMART, SCALABLE</b><br>IT SOLUTIONS.<br>DELIVERED.</h1>
<p class="abs hero-quote">“Our focus is to create amazing software and establish successful software firms”</p>
<div class="abs btn-slant" style="left:112px;top:468px;width:197px;height:53px">GET STARTED</div>

<!-- ABOUT -->
<div class="abs about-photo" role="img" aria-label="Group photo of the Velmorn IT team"></div>
<h2 class="abs heading" style="left:657px;top:804px;font-size:34px"><b>About</b> <span>Velmorn IT</span></h2>
<div class="abs about-text">
  <p>Our approach as a software development partner is distinct, as we prioritize collaboration and teamwork with our clients to deliver cutting-edge solutions. We will be there to assist in every aspect, starting from the conception of ideas to their execution.</p>
  <p>As an innovative technology group, we are committed to adopting a consistent and persistent approach that ensures our success while inspiring our partners and clients.</p>
</div>
<div class="abs btn-slant" style="left:657px;top:1107px;width:155px;height:48px;font-size:13px;padding-left:22px">LEARN MORE</div>

<!-- SERVICES -->
<svg class="abs" style="left:0;top:1280px" width="1200" height="920" viewBox="0 0 1200 920">
  <polygon points="0,5 1035,128 1200,38 1200,10 0,0" fill="#ffffff"/>
  <polygon points="0,5 1035,128 1200,38 1200,800 240,810 0,900" fill="#0f1a45"/>
  <polygon points="1040,128 1200,40 1200,75 1090,128" fill="#7fb2cf"/>
  <polygon points="0,900 240,805 1200,800 1200,920 0,920" fill="#7fb2cf"/>
  <polygon points="0,920 250,830 1200,920" fill="#ffffff"/>
</svg>
<h2 class="abs heading" style="left:0;top:1440px;width:1200px;text-align:center;font-size:38px;color:var(--white)"><span style="color:var(--blue);font-weight:300">OUR</span> <b style="color:var(--white)">SERVICES</b></h2>
<div class="underline" style="top:1500px;background:var(--blue)"></div>

<div class="abs svc" style="left:96px;top:1565px">
  <div class="svc-ring"><div class="svc-core">
    <svg width="70" height="60" viewBox="0 0 70 60" fill="none" stroke="#fff" stroke-width="2.5"><circle cx="35" cy="16" r="8"/><circle cx="15" cy="20" r="6"/><circle cx="55" cy="20" r="6"/><path d="M20 48v-8a15 15 0 0 1 30 0v8M4 48v-6a11 11 0 0 1 14-10M66 48v-6a11 11 0 0 0-14-10"/></svg>
  </div></div>
  <h3>IT Staffing &amp; Resource<br>Augmentation</h3>
  <p>As your trusted advisor, we help navigate complex IT decisions by understanding your unique business challenges.</p>
  <span class="pill">READ MORE</span>
</div>
<div class="abs svc" style="left:349px;top:1618px">
  <div class="svc-ring"><div class="svc-core">
    <svg width="66" height="60" viewBox="0 0 66 60" fill="none" stroke="#fff" stroke-width="2.5"><rect x="4" y="4" width="58" height="40" rx="3"/><path d="M4 12h58M26 52h14M33 44v8M26 22l-6 6 6 6M40 22l6 6-6 6M35 20l-4 16"/></svg>
  </div></div>
  <h3>Custom Application<br>Development</h3>
  <p>Transform your business foundation with expertly designed cloud infrastructure. Through our strategic partnerships with industry</p>
  <span class="pill">READ MORE</span>
</div>
<div class="abs svc" style="left:601px;top:1565px">
  <div class="svc-ring"><div class="svc-core on">
    <svg width="64" height="64" viewBox="0 0 64 64" fill="none" stroke="#fff" stroke-width="2.5"><circle cx="38" cy="38" r="10"/><path d="M38 22v6M38 48v6M22 38h6M48 38h6M27 27l4 4M45 45l4 4M49 27l-4 4M27 49l4-4"/><circle cx="20" cy="18" r="10"/><path d="M20 12v12M16 15h6a2.5 2.5 0 0 1 0 5h-4a2.5 2.5 0 0 0 0 5h6"/></svg>
  </div></div>
  <h3>System Integration<br>&amp; Automation</h3>
  <p>Navigate your cloud journey with confidence. As your trusted advisor, we help determine the right cloud strategy - whether public,</p>
  <span class="pill on">READ MORE</span>
</div>
<div class="abs svc" style="left:853px;top:1618px">
  <div class="svc-ring"><div class="svc-core">
    <svg width="70" height="60" viewBox="0 0 70 60" fill="none" stroke="#fff" stroke-width="2.5"><path d="M18 48a12 12 0 0 1 0-24 16 16 0 0 1 31-2 12 12 0 0 1 3 26z"/><circle cx="35" cy="32" r="7"/><path d="M32 39h6v6h-6zM35 10V4M22 14l-4-4M48 14l4-4"/></svg>
  </div></div>
  <h3>Cloud Solutions &amp;<br>DevOps</h3>
  <p>Protect your business with enterprise-grade security solutions backed by expert guidance. We leverage our partnerships</p>
  <span class="pill">READ MORE</span>
</div>

<!-- TESTIMONIALS -->
<h2 class="abs heading" style="left:0;top:2250px;width:1200px;text-align:center;font-size:34px"><b>Client</b> <span>Testimonials</span></h2>
<div class="underline" style="top:2302px"></div>
<div class="abs arrow-big" style="left:40px;top:2440px">‹</div>
<div class="abs arrow-big" style="left:1132px;top:2440px">›</div>

<div class="abs t-card" style="left:176px;top:2356px">
  <div class="abs t-body">
    <div class="t-quote">“</div>
    <p>Sed ut perspiciatis unde omnis iste natus sit voluptatem accusantium doloremque laudantium, totam rem aperiam,</p>
    <div class="t-name">John Doe</div>
    <div class="stars">★★★★★</div>
  </div>
</div>
<div class="abs t-avatar" style="left:123px;top:2414px" role="img" aria-label="Portrait of client John Doe"></div>

<div class="abs t-card" style="left:666px;top:2356px">
  <div class="abs t-body">
    <div class="t-quote">“</div>
    <p>Sed ut perspiciatis unde omnis iste natus sit voluptatem accusantium doloremque laudantium, totam rem aperiam,</p>
    <div class="t-name">John Doe</div>
    <div class="stars">★★★★★</div>
  </div>
</div>
<div class="abs t-avatar" style="left:613px;top:2414px" role="img" aria-label="Portrait of client John Doe"></div>

<!-- CLIENTS -->
<div class="abs client-band"></div>
<h2 class="abs heading" style="left:0;top:2736px;width:1200px;text-align:center;font-size:34px"><b>Our</b> <span>Client</span></h2>
<div class="underline" style="top:2788px"></div>
<div class="abs circ-arrow" style="left:41px;top:2863px"><svg width="10" height="12" viewBox="0 0 10 12"><polygon points="8,0 0,6 8,12" fill="#1b1f2a"/></svg></div>
<div class="abs circ-arrow" style="left:1123px;top:2863px"><svg width="10" height="12" viewBox="0 0 10 12"><polygon points="2,0 10,6 2,12" fill="#1b1f2a"/></svg></div>
<div class="abs logo-card" style="left:118px"><i></i>Plumtrex</div>
<div class="abs logo-card" style="left:318px">Summit Thread</div>
<div class="abs logo-card" style="left:515px">Payverra</div>
<div class="abs logo-card" style="left:715px">Marketloop</div>
<div class="abs logo-card" style="left:913px"><i></i>Brightgear</div>

<!-- CASE STUDIES -->
<h2 class="abs heading" style="left:0;top:3050px;width:1200px;text-align:center;font-size:34px"><b>Case</b> <span>Studies</span></h2>
<div class="underline" style="top:3102px"></div>

<div class="abs case" style="left:112px">
  <div class="abs case-img" role="img" aria-label="Server room with glowing cloud display" style="background:linear-gradient(180deg,#0c2a44,#1f6b8f 60%,#0b2036)"></div>
  <div class="abs case-box">
    <div class="case-meta">30 MAY 2024 &nbsp;/&nbsp; JOHN DOE</div>
    <h4>Lorem ipsum dolor sit amet, consectetur elit,</h4>
    <p>Sed ut perspiciatis unde omnis iste natus error sit voluptatem</p>
  </div>
</div>
<div class="abs case" style="left:445px">
  <div class="abs case-img" role="img" aria-label="Developers coding at computers in a dark office" style="background:linear-gradient(180deg,#2a2420,#5b4a3a 55%,#1d1a18)"></div>
  <div class="abs case-box">
    <div class="case-meta" style="color:var(--blue-mid)">30 MAY 2024 &nbsp;/&nbsp; JOHN DOE</div>
    <h4>Lorem ipsum dolor sit amet, consectetur elit,</h4>
    <p>Sed ut perspiciatis unde omnis iste natus error sit voluptatem</p>
    <div class="abs" style="left:0;bottom:0;width:190px;height:4px;background:var(--blue)"></div>
  </div>
</div>
<div class="abs case" style="left:775px">
  <div class="abs case-img" role="img" aria-label="Colleagues collaborating around a desk" style="background:linear-gradient(180deg,#d6d9dc,#8e8478 60%,#565149)"></div>
  <div class="abs case-box">
    <div class="case-meta">30 MAY 2024 &nbsp;/&nbsp; JOHN DOE</div>
    <h4>Lorem ipsum dolor sit amet, consectetur elit,</h4>
    <p>Sed ut perspiciatis unde omnis iste natus error sit voluptatem</p>
  </div>
</div>

<!-- CONTACT -->
<svg class="abs" style="left:0;top:3590px" width="1200" height="790" viewBox="0 0 1200 790">
  <polygon points="0,0 1200,85 1200,680 190,660 0,752" fill="#7fb2cf"/>
  <polygon points="1040,190 1200,72 1200,135 1080,190" fill="#0f1a45"/>
  <polygon points="0,752 190,660 1200,680 1200,790 0,790" fill="#0a1236"/>
  <polygon points="0,790 200,690 1200,790" fill="#ffffff"/>
</svg>
<h2 class="abs heading" style="left:0;top:3745px;width:1200px;text-align:center;font-size:38px;color:var(--navy)"><b style="color:var(--navy)">CONTACT</b> <span style="color:var(--navy)">US</span></h2>
<div class="underline" style="top:3802px;background:var(--navy)"></div>
<div class="abs field" style="left:184px;top:3857px;width:408px;height:49px">First Name *</div>
<div class="abs field" style="left:606px;top:3857px;width:409px;height:49px">Last Name *</div>
<div class="abs field" style="left:184px;top:3924px;width:408px;height:49px">Phone Number *</div>
<div class="abs field" style="left:606px;top:3924px;width:409px;height:49px">Email Address *</div>
<div class="abs field" style="left:184px;top:3990px;width:831px;height:91px;align-items:flex-start;padding-top:16px">Message</div>
<div class="abs submit">SUBMIT NOW</div>

<!-- FOOTER -->
<div class="abs" style="left:112px;top:4392px;width:190px;text-align:center">
  <div class="brand-mark" style="width:90px;height:90px;margin:0 auto 20px"></div>
  <div class="brand" style="font-size:24px">VELMORNIT</div>
</div>
<div class="abs social" style="left:152px;top:4553px" role="img" aria-label="Social profile"></div>
<div class="abs social" style="left:192px;top:4553px" role="img" aria-label="Social profile"></div>
<div class="abs social" style="left:232px;top:4553px" role="img" aria-label="Social profile"></div>

<div class="abs f-col" style="left:386px;top:4400px">
  <h5>Quick Links</h5>
  <ul><li>Home</li><li>About Us</li><li>Services</li><li>Case Studies</li><li>Careers</li><li>Contact</li></ul>
</div>
<div class="abs f-col" style="left:592px;top:4400px">
  <h5>About Company</h5>
  <ul><li>Privacy Policy</li><li>Terms of Service</li><li>Site Map</li><li>Imprint</li><li>Terms And Conditions</li></ul>
</div>
<div class="abs f-col" style="left:828px;top:4400px">
  <h5>Contact Us</h5>
</div>
<svg class="abs" style="left:826px;top:4444px" width="14" height="140" viewBox="0 0 14 140" fill="#5d97bb">
  <path d="M3 1c1-1 3 0 4 2l1 2c0 1 0 2-1 3 1 2 2 3 4 4 1-1 2-1 3-1v4c-6 0-11-5-11-11z"/>
  <rect x="1" y="51" width="12" height="9" rx="1"/><path d="M1 52l6 5 6-5" stroke="#fff" fill="none"/>
  <path d="M7 100a5 5 0 0 1 5 5c0 4-5 9-5 9s-5-5-5-9a5 5 0 0 1 5-5z"/><circle cx="7" cy="105" r="2" fill="#fff"/>
</svg>
<div class="abs f-contact" style="left:851px;top:4444px"><b>Opening Hours</b>Mon - Fri 8:30 AM to 5:30 PM</div>
<div class="abs f-contact" style="left:851px;top:4495px"><b>Email</b>admin@velmornit.com</div>
<div class="abs f-contact" style="left:851px;top:4545px"><b>Location</b>Ridgeway, Kestrel Town<br>(Lumen Tower)</div>

<div class="abs" style="left:112px;top:4616px;width:976px;height:1px;background:#d8dce1"></div>
<div class="abs" style="left:1107px;top:4597px;width:34px;height:34px;border-radius:50%;background:var(--blue);display:flex;align-items:center;justify-content:center">
  <svg width="12" height="8" viewBox="0 0 12 8"><path d="M1 7l5-5 5 5" stroke="#fff" stroke-width="2" fill="none"/></svg>
</div>
<div class="abs" style="left:0;top:4642px;width:1200px;text-align:center;font-size:13px;color:var(--text)">2025 Copyright - &nbsp;Velmorn IT. &nbsp;| All Rights Reserved</div>

</body>
</html>
```